Website for software company "velbra"

We need a website for our software company/startup named "velbra". We are developing several products (currently 3 standard-software products) which are all in different sectors, but all our products are available for Laptops/PC/Mobile Phones/Tablets, ... We do also create custom software and support our customers with consulting to optimize their processes.
We already have a Logo which you can find in the attached files.
We are a young team of 4 members (two founders and 2 employees).

To get an idea of our products -> the first one is a planning software for healthcare organizations (eg. Mercyway, firebrigade, pharmacy), the second one is a booking software for sport clubs and the third one is a competition software for sports hunting. You see very diverse. Include or ignore this info of our products as you like.

The design has to be a bootstrap 4 (or higher) design. We have licenced FontAwesome as iconset. Responsive design should come without saying.

Coding

Coded - Design and coding required

Number of Pages Required

5+ page

Font styles to use
Sans Serif

Requirements
Must have
• Starting page, product pages, news section, contact, team, services

```html
<!DOCTYPE html>
<html lang="en">
<head>
<meta charset="utf-8">
<title>velbra — Building Powerful Software</title>
<link href="https://fonts.googleapis.com/css2?family=Nunito+Sans:wght@400;600;700;800&display=swap" rel="stylesheet">
<style>
:root{
  --orange:#f58634;
  --orange-soft:#fde3cf;
  --ink:#111111;
  --muted:#6e6e76;
  --light:#a9a9b0;
  --bg-soft:#f5f5f7;
  --dark:#3a3a3a;
  --white:#ffffff;
  --line:#e9e9ee;
  --client:#1d3a78;
}
*{box-sizing:border-box;margin:0;padding:0}
html,body{width:1200px;height:3873px;overflow:hidden}
body{font-family:"Nunito Sans",Arial,sans-serif;color:var(--ink);background:var(--white);position:relative}
section,header,footer{position:absolute;left:0;width:1200px}
.abs{position:absolute}
.btn{position:absolute;background:var(--orange);color:var(--white);font-weight:800;font-size:15px;display:flex;align-items:center;justify-content:center;text-transform:uppercase;letter-spacing:.3px}
.brand{position:absolute;font-weight:800;letter-spacing:1px;display:flex;align-items:center;gap:10px;line-height:1}
.brand-mark{width:16px;height:16px;background:var(--orange)}

/* hero */
.hero{top:0;height:620px;background:linear-gradient(115deg,#1d2226 0%,#3b4349 45%,#59646b 70%,#2a3035 100%)}
.hero-photo{position:absolute;inset:0;background:radial-gradient(ellipse at 70% 40%,rgba(120,140,150,.45),rgba(20,24,28,.2) 60%)}
.hero .brand{left:116px;top:40px;font-size:38px;color:var(--white)}
.nav{position:absolute;left:515px;top:44px;display:flex;gap:23px;font-size:16px;color:#e6e6e6}
.nav-contact{position:absolute;left:937px;top:30px;width:131px;height:48px;border:2px solid var(--orange);color:var(--white);font-size:16px;display:flex;align-items:center;justify-content:center}
.hero h1{position:absolute;left:116px;top:234px;font-size:60px;line-height:64px;color:var(--white);font-weight:800}
.hero h1 span{font-weight:400}
.hero .sub{position:absolute;left:116px;top:370px;font-size:21px;color:var(--white)}

/* about */
.about{top:620px;height:442px;background:var(--bg-soft);text-align:center}
.eyebrow{color:var(--orange);font-size:15px}
.about .eyebrow{position:absolute;top:83px;width:100%}
.h2{font-size:35px;line-height:46px;font-weight:800;text-transform:uppercase}
.about .h2{position:absolute;top:103px;width:100%}
.about p{position:absolute;left:225px;width:750px;top:220px;font-size:13.5px;line-height:21px;color:var(--muted)}

/* services */
.services{top:1062px;height:675px}
.services .h2{position:absolute;left:92px;top:121px}
.services .lead{position:absolute;left:677px;top:125px;width:430px;font-size:13.5px;line-height:21px;color:var(--muted)}
.arrow{position:absolute;width:31px;height:31px;border:1px solid #dcdce2;border-radius:50%;display:flex;align-items:center;justify-content:center;background:var(--white)}
.card{position:absolute;top:274px;width:234px;height:282px;border:1px solid var(--line);background:var(--white);padding:0 23px}
.card.active{box-shadow:0 6px 22px rgba(0,0,0,.12);border-color:transparent}
.card .icon{position:absolute;left:12px;top:20px}
.card h3{position:absolute;left:23px;right:14px;top:100px;font-size:15px;font-weight:700;text-transform:uppercase;line-height:18px;height:36px;display:flex;align-items:center}
.card p{position:absolute;left:23px;right:20px;top:138px;font-size:13px;line-height:21px;color:var(--light)}
.card .more{position:absolute;left:23px;top:246px;font-size:13px;color:#555;display:flex;align-items:center;gap:8px}
.card.active .more{color:var(--orange)}

/* projects */
.projects{top:1737px;height:525px}
.projects .title{position:absolute;left:701px;top:90px}
.projects p{position:absolute;left:701px;width:400px;font-size:12.5px;line-height:19px;color:var(--muted)}
.dashboard{position:absolute;left:87px;top:125px;width:572px;height:274px}

/* work */
.work{top:2262px;height:871px;text-align:center}
.work .h2{position:absolute;top:125px;width:100%}
.work .lead{position:absolute;top:185px;left:340px;width:520px;font-size:13.5px;line-height:19px;color:var(--muted)}
.wcard{position:absolute;top:257px;width:324px;height:429px;background:var(--white);box-shadow:0 4px 18px rgba(0,0,0,.08);text-align:left}
.wcard .shot{height:278px;background:linear-gradient(135deg,#1c3a4a 0%,#1d6b84 50%,#29c2c9 80%,#13262f 100%)}
.wcard .client{position:absolute;left:23px;top:304px;font-size:18px;font-weight:800;color:var(--client)}
.tag{position:absolute;right:18px;top:302px;padding:4px 13px;border-radius:14px;background:#f2f2f4;font-size:12.5px;color:#9a9aa2}
.wcard p{position:absolute;left:23px;right:23px;top:348px;font-size:14px;line-height:21px;font-weight:600;color:#333}

/* cta */
.cta{top:3133px;height:343px;background:var(--dark);overflow:hidden;text-align:center;color:var(--white)}
.cta h2{position:absolute;top:80px;width:100%;font-size:33px;font-weight:700}
.cta p{position:absolute;top:143px;left:290px;width:620px;font-size:13.5px;line-height:21px;color:#e4e4e4}
.cta .btn{left:519px;top:220px;width:162px;height:45px;text-transform:none;font-weight:600;font-size:16px}
.cta-devices{position:absolute;left:0;top:40px;width:270px;height:257px;background:linear-gradient(150deg,#cfd7dc 0%,#7f99a8 45%,#1e2f3c 100%);clip-path:polygon(0 14%,55% 0,100% 35%,100% 78%,45% 100%,0 86%)}

/* footer */
.footer{top:3476px;height:397px}
.footer .brand{left:92px;top:92px;font-size:38px;color:var(--ink)}
.subscribe{position:absolute;left:92px;top:149px;width:311px;height:42px;border:1px solid #dedee4;font-size:12px;color:var(--light);padding:13px 16px}
.subscribe-btn{position:absolute;right:-1px;top:-1px;width:42px;height:42px;background:var(--orange);display:flex;align-items:center;justify-content:center}
.social{position:absolute;top:215px;width:31px;height:31px;border-radius:50%;background:#f1f1f3}
.fcol{position:absolute;top:98px}
.fcol h4{font-size:18px;font-weight:700;margin-bottom:12px}
.fcol li{list-style:none;font-size:15px;color:#8a8a92;line-height:28.5px}
.totop{position:absolute;left:1066px;top:296px;width:42px;height:42px;border-radius:50%;background:var(--orange);box-shadow:0 4px 10px rgba(245,134,52,.4);display:flex;align-items:center;justify-content:center}
.copy{position:absolute;left:92px;top:343px;font-size:11.5px;color:#333}
.copy span{color:var(--orange);text-decoration:underline}
</style>
</head>
<body>

<header class="hero">
  <div class="hero-photo" role="img" aria-label="Photo of a developer working at screens full of code"></div>
  <div class="brand"><span class="brand-mark"></span>VELBRA</div>
  <nav class="nav"><span>Home</span><span>Services</span><span>Team</span><span>Our Works</span><span>Eng ⌄</span></nav>
  <div class="nav-contact">Contact Us</div>
  <h1>BUILDING <span>POWERFUL</span><br>SOFTWARE</h1>
  <div class="sub">Transforming Ideas Into Solutions</div>
  <div class="btn" style="left:116px;top:429px;width:191px;height:49px">Start a Project</div>
</header>

<section class="about">
  <div class="eyebrow">About Us</div>
  <h2 class="h2">Company Development Depends<br>On Software</h2>
  <p>Lorem Ipsum Dolor Sit Amet, Consectetur Adipiscing Elit. Cras Lacus, Velit Ridiculus Elementum. Facilisi Ipsum, Scelerisque Sapien Vitae, Quis Faucibus.Facilisis Lectus Lacus Aliquam Sem Lectus Massa Hac Odio Tristique. Sagittis Ut Sed Neque Odio.Leo Habitant Sollicitudin Dui Nullam Nullam Sapien Praesent. Commodo Scelerisque Varius Cras Curabitur Augue Aliquam Risus.</p>
  <div class="btn" style="left:528px;top:334px;width:144px;height:49px">Read More</div>
</section>

<section class="services">
  <h2 class="h2" style="text-align:left">Trusted Software<br>Development Company</h2>
  <p class="lead">Lorem Ipsum Dolor Sit Amet, Consectetur Adipiscing Elit. Cras Lacus, Velit Ridiculus Elementum. Facilisi Ipsum, Scelerisque Sapien Vitae, Quis Faucibus.Facilisis Lectus Lacus Aliquam Sem Lectus Massa Hac Odio Tristique.</p>
  <div class="arrow" style="left:1038px;top:221px"><svg width="8" height="10"><path d="M6 1L2 5l4 4" stroke="#999" fill="none"/></svg></div>
  <div class="arrow" style="left:1078px;top:221px"><svg width="8" height="10"><path d="M2 1l4 4-4 4" stroke="#999" fill="none"/></svg></div>

  <div class="card" style="left:92px">
    <svg class="icon" width="70" height="70"><circle cx="22" cy="24" r="20" fill="var(--orange-soft)"/><rect x="18" y="18" width="42" height="30" fill="none" stroke="#333" stroke-width="2"/><path d="M39 24l9 5v9l-9 5-9-5v-9z" fill="none" stroke="var(--orange)" stroke-width="2"/><path d="M32 48v8M46 48v8M28 57h22" stroke="#333" stroke-width="2"/></svg>
    <h3>Product Design</h3>
    <p>Lorem ipsum dolor sit amet, consectetur adipiscing elit. Cras lacus, velit ridiculus elementum</p>
    <div class="more">READ MORE <svg width="5" height="8"><path d="M0 0l5 4-5 4z" fill="#333"/></svg></div>
  </div>
  <div class="card active" style="left:352px">
    <svg class="icon" width="70" height="70"><circle cx="22" cy="24" r="20" fill="var(--orange-soft)"/><rect x="22" y="12" width="30" height="40" fill="none" stroke="#333" stroke-width="2"/><rect x="27" y="18" width="20" height="13" fill="none" stroke="var(--orange)" stroke-width="2"/><path d="M18 52h38v5H18z" fill="none" stroke="#333" stroke-width="2"/><path d="M28 38h18M28 44h18" stroke="#333" stroke-width="2"/></svg>
    <h3>Web Development</h3>
    <p>Lorem ipsum dolor sit amet, consectetur adipiscing elit. Cras lacus, velit ridiculus elementum</p>
    <div class="more">READ MORE <svg width="5" height="8"><path d="M0 0l5 4-5 4z" fill="var(--orange)"/></svg></div>
  </div>
  <div class="card" style="left:613px">
    <svg class="icon" width="70" height="70"><circle cx="22" cy="24" r="20" fill="var(--orange-soft)"/><rect x="16" y="14" width="24" height="40" rx="3" fill="none" stroke="#333" stroke-width="2"/><rect x="40" y="26" width="18" height="12" fill="none" stroke="var(--orange)" stroke-width="2"/><path d="M22 24h12M22 32h12M22 40h8" stroke="var(--orange)" stroke-width="2"/></svg>
    <h3>App Development &amp; Integration</h3>
    <p>Lorem ipsum dolor sit amet, consectetur adipiscing elit. Cras lacus, velit ridiculus elementum</p>
    <div class="more">READ MORE <svg width="5" height="8"><path d="M0 0l5 4-5 4z" fill="#333"/></svg></div>
  </div>
  <div class="card" style="left:874px">
    <svg class="icon" width="70" height="70"><circle cx="22" cy="24" r="20" fill="var(--orange-soft)"/><circle cx="44" cy="26" r="11" fill="none" stroke="var(--orange)" stroke-width="2" stroke-dasharray="4 2"/><circle cx="44" cy="26" r="4" fill="none" stroke="#333" stroke-width="2"/><circle cx="26" cy="40" r="9" fill="none" stroke="#333" stroke-width="2" stroke-dasharray="4 2"/><path d="M18 54l8-6 8 6" fill="none" stroke="#333" stroke-width="2"/></svg>
    <h3>Project Management</h3>
    <p>Lorem ipsum dolor sit amet, consectetur adipiscing elit. Cras lacus, velit ridiculus elementum</p>
    <div class="more">READ MORE <svg width="5" height="8"><path d="M0 0l5 4-5 4z" fill="#333"/></svg></div>
  </div>
</section>

<section class="projects">
  <svg class="abs" style="left:0;top:0" width="1200" height="525"><polygon points="600,0 1200,0 1200,525 180,525" fill="var(--bg-soft)"/><polygon points="0,59 558,59 180,525 0,525" fill="var(--orange)"/></svg>
  <div class="dashboard" role="img" aria-label="Laptop and chart card showing a dashboard with bar charts, a world map and statistics">
    <div class="abs" style="left:130px;top:0;width:390px;height:262px;background:linear-gradient(160deg,#ffffff 0%,#eef2f8 100%);border:8px solid #2a2a2e;border-radius:10px 10px 0 0"></div>
    <div class="abs" style="left:80px;top:258px;width:492px;height:16px;background:linear-gradient(#b8b8bd,#6f6f74);border-radius:0 0 12px 12px"></div>
    <div class="abs" style="left:0;top:112px;width:230px;height:130px;background:linear-gradient(160deg,#ffffff,#f1f3f7);box-shadow:0 8px 20px rgba(0,0,0,.18)"></div>
  </div>
  <h2 class="h2 title">We Bring Software<br>Projects To Life</h2>
  <p style="top:197px">Lorem Ipsum Dolor Sit Amet, Consectetur Adipiscing Elit. Cras Lacus, Velit Ridiculus Elementum. Facilisi Ipsum, Scelerisque Sapien Vitae, Quis Faucibus.</p>
  <p style="top:269px">Facilisis Lectus Lacus Aliquam Sem Lectus Massa Hac Odio Tristique. Sagittis Ut Sed Neque Odio.Leo Habitant Sollicitudin Dui Nullam Nullam Sapien Praesent. Commodo Scelerisque Varius Cras Curabitur Augue Aliquam Risus.</p>
  <div class="btn" style="left:701px;top:387px;width:156px;height:49px">Contact Us</div>
</section>

<section class="work">
  <h2 class="h2">Our Work</h2>
  <p class="lead">Lorem Ipsum Dolor Sit Amet, Consectetur Adipiscing Elit. Cras Lacus, Velit Ridiculus Elementum. Facilisi Ipsum, Scelerisque Sapien Vitae, Quis Faucibus.</p>
  <div class="wcard" style="left:90px"><div class="shot" role="img" aria-label="Website mockups on tablet and phone screens"></div><div class="client">Corvalen Media</div><div class="tag">WEBSITE</div><p>Lorem ipsum dolor sit amet, consectetur adipiscing elit.</p></div>
  <div class="wcard" style="left:438px"><div class="shot" role="img" aria-label="Website mockups on tablet and phone screens"></div><div class="client">Corvalen Media</div><div class="tag">WEBSITE</div><p>Lorem ipsum dolor sit amet, consectetur adipiscing elit.</p></div>
  <div class="wcard" style="left:787px"><div class="shot" role="img" aria-label="Website mockups on tablet and phone screens"></div><div class="client">Corvalen Media</div><div class="tag">WEBSITE</div><p>Lorem ipsum dolor sit amet, consectetur adipiscing elit.</p></div>
  <div class="arrow" style="left:564px;top:728px"><svg width="8" height="10"><path d="M6 1L2 5l4 4" stroke="#999" fill="none"/></svg></div>
  <div class="arrow" style="left:604px;top:728px"><svg width="8" height="10"><path d="M2 1l4 4-4 4" stroke="#999" fill="none"/></svg></div>
</section>

<section class="cta">
  <svg class="abs" style="left:0;top:0" width="1200" height="343"><polygon points="780,0 1010,0 950,130" fill="#444"/><polygon points="950,130 1160,20 1200,120 1150,310" fill="#555"/><polygon points="950,130 1150,310 1060,343 980,343" fill="#4a4a4a"/><polygon points="1160,20 1200,0 1200,120" fill="#5f5f5f"/></svg>
  <div class="cta-devices" role="img" aria-label="Tablets and laptops displaying website designs"></div>
  <h2>Let’s Start Your Project</h2>
  <p>Facilisis Lectus Lacus Aliquam Sem Lectus Massa Hac Odio Tristique. Sagittis Ut Sed Neque Odio.Leo Habitant Sollicitudin Dui Nullam Nullam Sapien Praesent. Commodo Scelerisque Varius Cras Curabitur Augue Aliquam Risus.</p>
  <div class="btn">Start A Project</div>
</section>

<footer class="footer">
  <div class="brand"><span class="brand-mark"></span>VELBRA</div>
  <div class="subscribe">Email here<div class="subscribe-btn"><svg width="16" height="16"><path d="M1 7L15 1 10 15 8 9z" fill="#fff"/></svg></div></div>
  <div class="social" style="left:90px" aria-label="Social profile"></div>
  <div class="social" style="left:136px" aria-label="Social profile"></div>
  <div class="social" style="left:180px" aria-label="Social profile"></div>
  <div class="fcol" style="left:529px"><h4>Quick Links</h4><ul><li>Home</li><li>Services</li><li>Team</li><li>Our Works</li><li>Contact Us</li></ul></div>
  <div class="fcol" style="left:713px"><h4>Services</h4><ul><li>Product Design</li><li>Web Development</li><li>APP Development &amp; Integration</li><li>Project Management</li><li>Security &amp; Privacy</li><li>Enterprise Solutions</li></ul></div>
  <div class="fcol" style="left:980px"><h4>Legal</h4><ul><li>Support</li><li>Terms &amp; Condition</li><li>Privacy Policy</li></ul></div>
  <div class="totop"><svg width="14" height="9"><path d="M1 8l6-6 6 6" stroke="#fff" stroke-width="2" fill="none"/></svg></div>
  <div class="copy">©Copyright 2022. <span>VELBRA</span> | All Rights Reserved</div>
</footer>

</body>
</html>
```